fizzy drinks label design

I want to design fizzy drink label for 3 flavors : black grapes, red apple and mojito, band name kestrova, product name TOLMA , product will be in plastic bottle, label size 198 mm X 66mm

```html
<!DOCTYPE html>
<html lang="en">
<head>
<meta charset="utf-8">
<title>kestrova TOLMA – fizzy drink labels</title>
<link rel="stylesheet" href="https://fonts.googleapis.com/css2?family=Kaushan+Script&display=swap">
<style>
  :root {
    --canvas-bg: #f4f4f4;
    --white: #ffffff;
    --grape-main: #8a2fa8;
    --grape-dark: #62207e;
    --grape-art: #6b2f95;
    --mojito-main: #86bb33;
    --mojito-dark: #5f9422;
    --mojito-art: #a6d15a;
    --apple-main: #d2292e;
    --apple-dark: #a81c21;
    --apple-art: #b71f25;
  }
  * { box-sizing: border-box; margin: 0; padding: 0; }
  html, body {
    width: 1200px; height: 877px; overflow: hidden;
    background: var(--canvas-bg);
  }
  .label-sheet {
    width: 1200px; height: 877px;
    display: flex; flex-direction: column; align-items: center; justify-content: center;
    gap: 28px;
  }
  .label {
    position: relative;
    width: 750px; height: 250px;
    background: var(--main);
    overflow: hidden;
    box-shadow: 0 4px 14px rgba(0,0,0,0.12);
  }
  .label--grape  { --main: var(--grape-main);  --dark: var(--grape-dark);  --art: var(--grape-art); }
  .label--mojito { --main: var(--mojito-main); --dark: var(--mojito-dark); --art: var(--mojito-art); }
  .label--apple  { --main: var(--apple-main);  --dark: var(--apple-dark);  --art: var(--apple-art); }

  .label__waves { position: absolute; inset: 0; width: 100%; height: 100%; }
  .label__waves .wave-light { fill: var(--white); }
  .label__waves .wave-band  { fill: var(--dark); }

  .brand-tag {
    position: absolute; left: 240px; top: 12px;
    width: 130px; height: 46px;
    background: var(--dark);
    border: 3px solid var(--white);
    border-radius: 10px;
    display: flex; align-items: center; justify-content: center;
    font-family: "Kaushan Script", cursive;
    font-size: 24px; line-height: 1; color: var(--white);
  }
  .fruit-art {
    position: absolute; left: 400px; top: 6px;
    width: 160px; height: 62px;
    border-radius: 50%;
    background: radial-gradient(circle at 40% 40%, var(--art), var(--dark));
  }
  .product-name {
    position: absolute; left: 0; right: 0; top: 74px;
    text-align: center;
    font-family: "Kaushan Script", cursive;
    font-weight: 400;
    font-size: 92px; line-height: 1;
    color: var(--white);
  }
  .flavor-ribbon {
    position: absolute; left: 390px; top: 196px;
    width: 290px; height: 44px;
    background: var(--dark);
    display: flex; align-items: center; justify-content: center;
    font-family: "Kaushan Script", cursive;
    font-size: 26px; line-height: 1; color: var(--white);
    clip-path: polygon(0 0, 100% 0, 96% 50%, 100% 100%, 0 100%, 4% 50%);
  }
</style>
</head>
<body>
<main class="label-sheet">

  <section class="label label--grape">
    <svg class="label__waves" viewBox="0 0 750 250" aria-hidden="true">
      <path class="wave-light" d="M0 178 C150 155 250 200 375 182 S600 152 750 172 L750 215 C600 195 500 235 375 222 S150 205 0 225 Z"/>
      <path class="wave-band" d="M0 225 C150 205 250 222 375 222 S600 195 750 215 L750 250 L0 250 Z"/>
    </svg>
    <div class="brand-tag">kestrova</div>
    <div class="fruit-art" role="img" aria-label="Bunch of black grapes with a green leaf"></div>
    <h2 class="product-name">TOLMA</h2>
    <p class="flavor-ribbon">Black Grapes</p>
  </section>

  <section class="label label--mojito">
    <svg class="label__waves" viewBox="0 0 750 250" aria-hidden="true">
      <path class="wave-light" d="M0 178 C150 155 250 200 375 182 S600 152 750 172 L750 215 C600 195 500 235 375 222 S150 205 0 225 Z"/>
      <path class="wave-band" d="M0 225 C150 205 250 222 375 222 S600 195 750 215 L750 250 L0 250 Z"/>
    </svg>
    <div class="brand-tag">kestrova</div>
    <div class="fruit-art" role="img" aria-label="Lime slice with fresh mint leaves"></div>
    <h2 class="product-name">TOLMA</h2>
    <p class="flavor-ribbon">Mojito</p>
  </section>

  <section class="label label--apple">
    <svg class="label__waves" viewBox="0 0 750 250" aria-hidden="true">
      <path class="wave-light" d="M0 178 C150 155 250 200 375 182 S600 152 750 172 L750 215 C600 195 500 235 375 222 S150 205 0 225 Z"/>
      <path class="wave-band" d="M0 225 C150 205 250 222 375 222 S600 195 750 215 L750 250 L0 250 Z"/>
    </svg>
    <div class="brand-tag">kestrova</div>
    <div class="fruit-art" role="img" aria-label="Red apple with a halved apple and leaf"></div>
    <h2 class="product-name">TOLMA</h2>
    <p class="flavor-ribbon">Red Apple</p>
  </section>

</main>
</body>
</html>
```